business card design for luxurious real estate brand

using the attached logo, i am looking for a 2-sided business card design. the back should be the gold logo on black background. the front needs to include: gold logo, name, phone, email, and website

Industry/Entity Type

real estate

Contact Information for Business Card

logo, name, email, phone, website

Font styles to use
Sans Serif

```html
<!DOCTYPE html>
<html lang="en">
<head>
<meta charset="UTF-8">
<title>Casa Veloria Business Card</title>
<link href="https://fonts.googleapis.com/css2?family=Montserrat:wght@400;500;700&display=swap" rel="stylesheet">
<style>
  :root {
    --backdrop: #3a3a3b;
    --card-black: #221f20;
    --card-white: #ffffff;
    --gold: #c9a04a;
    --gold-light: #eccd85;
    --gold-dark: #a27c2e;
    --text-light: #f2f2f2;
  }
  * { margin: 0; padding: 0; box-sizing: border-box; }
  html, body {
    width: 1200px;
    height: 1200px;
    overflow: hidden;
    background: var(--backdrop);
    font-family: "Montserrat", Arial, sans-serif;
  }
  .canvas {
    position: relative;
    width: 1200px;
    height: 1200px;
  }
  .card {
    position: absolute;
    left: 220px;
    width: 760px;
    height: 434px;
    border-radius: 34px;
    overflow: hidden;
    box-shadow: 0 10px 30px rgba(0,0,0,0.45);
  }
  .card-front { top: 120px; background: var(--card-white); }
  .card-back { top: 646px; background: var(--card-black); }

  .front-panel {
    position: absolute;
    inset: 0;
    width: 760px;
    height: 434px;
  }

  .contact-block {
    position: absolute;
    left: 64px;
    top: 190px;
    color: var(--text-light);
  }
  .contact-name {
    font-weight: 700;
    font-size: 34px;
    letter-spacing: 0.5px;
    color: var(--gold);
    line-height: 1;
  }
  .contact-position {
    font-weight: 400;
    font-size: 16px;
    letter-spacing: 0.5px;
    margin-top: 4px;
  }
  .contact-list {
    list-style: none;
    margin-top: 22px;
    padding-left: 22px;
  }
  .contact-item {
    display: flex;
    align-items: center;
    gap: 12px;
    font-size: 17px;
    line-height: 1;
    margin-bottom: 11px;
  }
  .contact-icon { width: 20px; height: 20px; flex: none; }

  .brand {
    position: absolute;
    display: flex;
    align-items: center;
    color: var(--gold);
    font-weight: 500;
    text-transform: uppercase;
    white-space: nowrap;
  }
  .brand-square {
    background: var(--gold);
    flex: none;
  }
  .brand-front {
    left: 603px;
    top: 200px;
    transform: translate(-50%, -50%);
    font-size: 19px;
    letter-spacing: 3px;
    gap: 10px;
  }
  .brand-front .brand-square { width: 12px; height: 12px; }
  .brand-back {
    left: 50%;
    top: 50%;
    transform: translate(-50%, -50%);
    font-size: 46px;
    letter-spacing: 10px;
    gap: 24px;
  }
  .brand-back .brand-square { width: 26px; height: 26px; }
</style>
</head>
<body>
<main class="canvas">

  <section class="card card-front" aria-label="Business card front">
    <svg class="front-panel" viewBox="0 0 760 434" aria-hidden="true">
      <defs>
        <linearGradient id="goldLine" x1="0" y1="0" x2="0" y2="1">
          <stop offset="0" stop-color="#b8923f"/>
          <stop offset="0.45" stop-color="#eccd85"/>
          <stop offset="1" stop-color="#a27c2e"/>
        </linearGradient>
      </defs>
      <polygon points="0,0 300,0 418,150 418,434 0,434" fill="#221f20"/>
      <polyline points="328,0 446,146 446,434" fill="none" stroke="url(#goldLine)" stroke-width="7"/>
    </svg>

    <div class="contact-block">
      <div class="contact-name">FULL NAME</div>
      <div class="contact-position">POSITION</div>
      <ul class="contact-list">
        <li class="contact-item">
          <svg class="contact-icon" viewBox="0 0 24 24" aria-hidden="true"><path fill="#c9a04a" d="M6.6 10.8a15.2 15.2 0 0 0 6.6 6.6l2.2-2.2a1 1 0 0 1 1-.25 11.4 11.4 0 0 0 3.6.57 1 1 0 0 1 1 1V20a1 1 0 0 1-1 1A17 17 0 0 1 3 4a1 1 0 0 1 1-1h3.5a1 1 0 0 1 1 1c0 1.25.2 2.450.57 3.57a1 1 0 0 1-.25 1z"/></svg>
          <span>(000) 000 0000</span>
        </li>
        <li class="contact-item">
          <svg class="contact-icon" viewBox="0 0 24 24" aria-hidden="true"><rect x="2" y="5" width="20" height="14" rx="1" fill="#c9a04a"/><path d="M2.5 5.5 12 13l9.5-7.5" fill="none" stroke="#221f20" stroke-width="1.6"/></svg>
          <span>email@company.com</span>
        </li>
        <li class="contact-item">
          <svg class="contact-icon" viewBox="0 0 24 24" aria-hidden="true"><g fill="none" stroke="#c9a04a" stroke-width="1.6"><circle cx="12" cy="12" r="9.5"/><ellipse cx="12" cy="12" rx="4.2" ry="9.5"/><path d="M2.5 12h19M4 7h16M4 17h16"/></g></svg>
          <span>www.company.com</span>
        </li>
      </ul>
    </div>

    <div class="brand brand-front">
      <span class="brand-square" aria-hidden="true"></span>
      <span class="brand-name">Casa Veloria</span>
    </div>
  </section>

  <section class="card card-back" aria-label="Business card back">
    <div class="brand brand-back">
      <span class="brand-square" aria-hidden="true"></span>
      <span class="brand-name">Casa Veloria</span>
    </div>
  </section>

</main>
</body>
</html>
```